Business card design and logo needed - Photographer

I take photos of weddings, rodeos, snowmobiling.
Need a card to hand out to prospective clients.
Industry/Entity Type
Business
Contact Information for Business Card
Marlon Pettibrook Photography
Requirements
Must have
- Bold
Black or white base.
My website. www.MarlonPettibrook.com
Should not have
- camera/ lens/ aperture blades

```html
<!DOCTYPE html>
<html lang="en">
<head>
<meta charset="utf-8">
<title>Marlon Pettibrook Photography – Logo and Business Card</title>
<link rel="stylesheet" href="https://fonts.googleapis.com/css2?family=Marcellus&family=Open+Sans:wght@400&display=swap">
<style>
  :root {
    --page: #e9e9ea;
    --paper: #ffffff;
    --card: #2a2829;
    --card-edge: #1c1b1c;
    --plum: #8e4a93;
    --lilac: #b98dbf;
    --lilac-soft: #d8c3dc;
    --ink-light: #f2f0f2;
    --ink-muted: #c9c6c9;
    --rule: #4a474a;
  }
  * { box-sizing: border-box; margin: 0; padding: 0; }
  html, body { width: 1200px; height: 880px; overflow: hidden; }
  body {
    background: var(--page);
    font-family: "Open Sans", Arial, sans-serif;
    position: relative;
  }

  /* Logo lockup on white stock */
  .logo-sheet {
    position: absolute;
    left: 150px; top: 50px;
    width: 900px; height: 220px;
    background: var(--paper);
    display: flex; align-items: center; justify-content: center;
    gap: 26px;
  }
  .logo-mark {
    width: 74px; height: 74px;
    background: var(--lilac);
  }
  .logo-words { display: flex; flex-direction: column; }
  .logo-name {
    font-family: "Marcellus", Georgia, serif;
    font-size: 58px; line-height: 1;
    color: var(--plum);
  }
  .logo-tag {
    font-family: "Marcellus", Georgia, serif;
    font-size: 20px; letter-spacing: 13px;
    color: var(--lilac-soft);
    margin-top: 6px;
  }

  /* Business card, front */
  .card {
    position: absolute;
    left: 240px; top: 320px;
    width: 720px; height: 410px;
    background: linear-gradient(160deg, #333133 0%, var(--card) 55%, var(--card-edge) 100%);
    border-radius: 4px;
  }
  .card-mark {
    position: absolute;
    left: 70px; top: 70px;
    width: 120px; height: 120px;
    background: var(--lilac);
  }
  .card-identity {
    position: absolute;
    left: 300px; top: 78px;
    width: 360px;
    border-bottom: 1px solid var(--rule);
    padding-bottom: 12px;
  }
  .card-name {
    font-family: "Marcellus", Georgia, serif;
    font-size: 34px; line-height: 1.1;
    color: var(--ink-light);
  }
  .card-tag {
    font-family: "Marcellus", Georgia, serif;
    font-size: 15px; letter-spacing: 9px;
    color: var(--plum);
    margin-top: 4px;
  }
  .card-contacts {
    position: absolute;
    left: 300px; top: 210px;
    list-style: none;
  }
  .card-contacts li {
    display: flex; align-items: center; gap: 16px;
    font-size: 20px; line-height: 34px;
    color: var(--ink-muted);
  }
  .contact-icon { width: 18px; height: 18px; flex: none; }
  .contact-icon * { fill: none; stroke: var(--plum); stroke-width: 1.6; }
  .contact-icon .solid { fill: var(--plum); stroke: none; }
</style>
</head>
<body>

  <section class="logo-sheet">
    <div class="logo-mark"></div>
    <div class="logo-words">
      <span class="logo-name">Marlon Pettibrook</span>
      <span class="logo-tag">PHOTOGRAPHY</span>
    </div>
  </section>

  <section class="card">
    <div class="card-mark"></div>

    <div class="card-identity">
      <div class="card-name">Marlon Pettibrook</div>
      <div class="card-tag">PHOTOGRAPHY</div>
    </div>

    <ul class="card-contacts">
      <li>
        <svg class="contact-icon" viewBox="0 0 18 18" aria-hidden="true">
          <path class="solid" d="M2 6 Q9 1 16 6 L14 8 L11.5 6.5 L6.5 6.5 L4 8 Z"/>
          <rect class="solid" x="4" y="9" width="10" height="7" rx="1"/>
        </svg>
        <span>0144 555 678</span>
      </li>
      <li>
        <svg class="contact-icon" viewBox="0 0 18 18" aria-hidden="true">
          <rect x="1.5" y="4" width="15" height="10"/>
          <path d="M1.5 4 L9 10 L16.5 4"/>
        </svg>
        <span>MarlonPettibrook@email.com</span>
      </li>
      <li>
        <svg class="contact-icon" viewBox="0 0 18 18" aria-hidden="true">
          <circle class="solid" cx="9" cy="9" r="8"/>
          <path d="M1 9 H17 M9 1 V17 M3 4.5 H15 M3 13.5 H15" style="stroke:#2a2829;stroke-width:1.2"/>
        </svg>
        <span>www.MarlonPettibrook.com</span>
      </li>
    </ul>
  </section>

</body>
</html>
```